Baufirma sucht Design für Schafkopfkarten
Zielgruppe
Wir sind eine Baufirma und suchen ein schlichtes Design für unsere Schafkopfkarten. Unsere Zielgruppe ist bunt gemischt
Aufgabenstellung
Wir suchen nach einem Design für Schafkopfkarten/Spielkarten.
- Kartenformat 56 x 100 mm
- weißer Rand
- Schlicht
- eventuell Retro Design
- Firmenlogo soll nicht verändert werden
- eventuell 'seit 1946' integrieren

```html
<!DOCTYPE html>
<html lang="de">
<head>
<meta charset="utf-8">
<title>Warnholm – Spielkarten</title>
<link href="https://fonts.googleapis.com/css2?family=Roboto:wght@300;400;700;900&display=swap" rel="stylesheet">
<style>
  :root {
    --backdrop: #e8e8e8;
    --card: #ffffff;
    --ink: #000000;
    --slate: #474e52;
    --grey: #8a8c8f;
    --yellow: #ffde00;
  }
  html, body {
    margin: 0;
    width: 1200px;
    height: 1200px;
    overflow: hidden;
    background: var(--backdrop);
    font-family: "Roboto", Arial, sans-serif;
  }
  .card {
    position: absolute;
    top: 171px;
    width: 480px;
    height: 857px;
    background: var(--card);
    border-radius: 11px;
  }
  .card--front { left: 65px; }
  .card--back { left: 643px; }

  .corner-name {
    position: absolute;
    font-weight: 900;
    font-size: 13px;
    letter-spacing: 0.5px;
    color: var(--slate);
    line-height: 1;
  }
  .corner-name--top { left: 16px; top: 28px; }
  .corner-name--bottom { right: 16px; bottom: 28px; transform: rotate(180deg); }

  .since {
    position: absolute;
    display: flex;
    align-items: center;
    gap: 14px;
    white-space: nowrap;
    color: var(--ink);
    font-size: 18px;
    line-height: 1;
  }
  .since__word { font-weight: 900; letter-spacing: 1px; }
  .since__bar { width: 20px; height: 2px; background: var(--ink); display: none; }
  .since__rule { font-weight: 300; }
  .since__year { font-weight: 300; letter-spacing: 4px; }
  .since--top {
    left: 42px;
    top: 99px;
    transform-origin: 0 0;
    transform: rotate(90deg);
  }
  .since--bottom {
    left: 438px;
    top: 758px;
    transform-origin: 0 0;
    transform: rotate(-90deg);
  }

  .brand {
    position: absolute;
    left: 0;
    right: 0;
    top: 344px;
    text-align: center;
  }
  .brand__square {
    width: 60px;
    height: 60px;
    margin: 0 auto 30px;
    background: var(--yellow);
  }
  .brand__name {
    font-weight: 900;
    font-size: 44px;
    letter-spacing: 3px;
    color: var(--slate);
    line-height: 1;
  }
  .brand__services {
    margin-top: 16px;
    font-weight: 400;
    font-size: 16px;
    letter-spacing: 1px;
    color: var(--grey);
  }
  .brand__sep { color: var(--yellow); margin: 0 10px; }

  .back-name {
    position: absolute;
    left: 0;
    right: 0;
    top: 398px;
    text-align: center;
    font-weight: 900;
    font-size: 56px;
    letter-spacing: 3px;
    color: var(--slate);
    line-height: 1;
  }
</style>
</head>
<body>
  <section class="card card--front">
    <div class="corner-name corner-name--top">WARNHOLM</div>
    <div class="since since--top">
      <span class="since__word">SEIT</span>
      <span class="since__rule">|</span>
      <span class="since__year">1946</span>
    </div>

    <div class="brand">
      <div class="brand__square"></div>
      <div class="brand__name">WARNHOLM</div>
      <div class="brand__services">TIEFBAU<span class="brand__sep">//</span>ABBRUCH<span class="brand__sep">//</span>RECYCLING</div>
    </div>

    <div class="since since--bottom">
      <span class="since__word">SEIT</span>
      <span class="since__rule">|</span>
      <span class="since__year">1946</span>
    </div>
    <div class="corner-name corner-name--bottom">WARNHOLM</div>
  </section>

  <section class="card card--back">
    <div class="back-name">WARNHOLM</div>
  </section>
</body>
</html>
```